Collagen Tub Packaging Design for a New Brand

PLEASE DON'T SEND ANY NEW DESIGNS WE JUST HAVE TO DECIDE WITH MY PARTNERS THANKS A LOT.
I've created a very detailed document & design examples of what we like in certain designs and what we don't.

There are 3 documents:
1- Brief for the Design (please read it before designing)
2- Brand Design Examples that we like (and why we like them)
3- Die cut for the packaging design. This will be it's dimensions.

We are NOT looking for someone to micro-manage. In contrast, we want someone to help us express our ideas better with their design. Nothing I say in these briefs are there to limit the creativity of the designer, because if we knew exactly what we wanted we would do it ourselves but we trust the designer's expertise in this packaging design.

In short: We want our brand to feel premium, high-quality & trust worthy with it's design not feeling very busy or bloated. We don't have a logo source file, but you'll get the idea of what we want when you see it).

Let me know if you have any further questions, will answer each question real fast.

Thanks.

Target Market(s)

Pretty much everyone above 25+ in Turkey because nearly all of them are using are collagens so our audience is wild.

Industry/Entity Type

Collagen - Health, Wellness & Supplements

Font styles to use
Serif
Sans Serif

Colors

Designer to choose colors to be used in the design.

Requirements
Must have
• Our design should be distinct, a design style which everyone can identify from 10 meters away if they know the product. This is a MUST have for us. It's up to designer to achieve it. This can be just a simple color palette aswell.
Should not have
• It shouldn't feel bloated and very busy. Please avoid very detailed icons (as a rule of thumb, if you can make it work great)

```html
<!DOCTYPE html>
<html lang="en">
<head>
<meta charset="utf-8">
<title>Nuvella Collagen Tub Labels</title>
<link href="https://fonts.googleapis.com/css2?family=Ubuntu:wght@400;500;700&family=Montserrat:wght@400;600;800&display=swap" rel="stylesheet">
<style>
  :root {
    --stage: #000000;
    --violet: #a32fd4;
    --violet-deep: #9b00cc;
    --violet-soft: #b75ee0;
    --silver-light: #f2f2f2;
    --silver-mid: #bdbdbd;
    --silver-dark: #8a8a8a;
    --ink: #333333;
    --ink-soft: #5c5c5c;
    --teal: #1d4a48;
    --white: #ffffff;
  }
  * { box-sizing: border-box; margin: 0; padding: 0; }
  html, body { width: 1200px; height: 799px; overflow: hidden; background: var(--stage); }
  .canvas { position: relative; width: 1200px; height: 799px; background: var(--stage); }

  .label {
    position: absolute; left: 136px; width: 930px; height: 300px; overflow: hidden;
    font-family: "Montserrat", sans-serif;
  }
  .label--violet { top: 70px;
    --bg: radial-gradient(ellipse at 30% 40%, var(--violet-soft), var(--violet) 70%);
    --band: linear-gradient(90deg, var(--silver-dark), var(--silver-light) 30%, var(--silver-mid) 55%, var(--silver-light) 80%, var(--silver-dark));
    --tab: var(--violet-deep);
    --title: var(--violet-deep);
    --brand: var(--ink-soft);
    --plate-text: var(--violet-deep);
    --plate-edge: #8a8a8a;
    --body-text: var(--white);
    --stat-rule: var(--white);
  }
  .label--silver { top: 430px;
    --bg: radial-gradient(ellipse at 30% 40%, #efefef, #d6d6d6 75%);
    --band: var(--violet-deep);
    --tab: #333333;
    --title: var(--ink);
    --brand: var(--ink);
    --plate-text: var(--ink);
    --plate-edge: #3a3a3a;
    --body-text: var(--ink);
    --stat-rule: var(--ink);
  }

  .label__backdrop { position: absolute; inset: 0; background: var(--bg); }
  .label__band { position: absolute; left: 0; right: 0; background: var(--band); }
  .label__band--top { top: 12px; height: 6px; }
  .label__band--bottom { bottom: 0; height: 8px; }

  .front-panel {
    position: absolute; left: 322px; top: 0; width: 286px; height: 194px;
    background: radial-gradient(circle at 40% 45%, #ffffff, #ededed 55%, #dcdcdc);
  }

  .tab { position: absolute; top: 0; width: 38px; height: 32px; background: var(--tab); }
  .tab--capacity { left: 503px; }
  .tab--age { left: 548px; }
  .badge {
    position: absolute; top: 26px; width: 40px; height: 40px; border-radius: 50%;
    background: var(--white); border: 1.5px solid var(--teal);
    color: var(--teal); text-align: center; font-family: "Ubuntu", sans-serif;
  }
  .badge--capacity { left: 502px; }
  .badge--age { left: 547px; }
  .badge__caption { display: block; font-size: 3.6px; line-height: 4px; margin-top: 8px; letter-spacing: .2px; }
  .badge__value { display: block; font-size: 13px; font-weight: 500; line-height: 14px; }

  .brand { position: absolute; left: 336px; top: 30px; width: 110px; height: 34px; }
  .brand__name { font-family: "Ubuntu", sans-serif; font-weight: 500; font-size: 24px; color: var(--brand); line-height: 1; }
  .brand__tagline { position: absolute; left: 56px; top: 25px; font-family: "Ubuntu", sans-serif; font-weight: 700; font-size: 6px; color: var(--ink-soft); white-space: nowrap; }

  .product__kind { position: absolute; left: 342px; top: 77px; font-family: "Ubuntu", sans-serif; font-weight: 700; font-size: 12.5px; color: var(--ink-soft); letter-spacing: .2px; }
  .product__name { position: absolute; left: 335px; top: 86px; width: 252px; font-family: "Ubuntu", sans-serif; font-weight: 700; font-size: 50px; letter-spacing: -1.5px; color: var(--title); line-height: 1; text-align: right; }
  .product__sub { position: absolute; right: 345px; top: 139px; font-family: "Ubuntu", sans-serif; font-weight: 700; font-size: 13px; color: var(--ink-soft); }
  .product__uses { position: absolute; right: 343px; top: 158px; font-family: "Montserrat", sans-serif; font-weight: 800; font-size: 9.5px; color: var(--teal); letter-spacing: .6px; white-space: nowrap; }

  .plate { position: absolute; left: 322px; top: 179px; width: 172px; height: 28px; }
  .plate__text { position: absolute; left: 346px; top: 186px; font-family: "Montserrat", sans-serif; font-weight: 800; font-size: 12px; line-height: 14px; letter-spacing: 7.6px; color: var(--plate-text); }

  .benefits { position: absolute; left: 343px; top: 213px; list-style: none; }
  .benefits li { position: relative; padding-left: 8px; font-family: "Montserrat", sans-serif; font-weight: 800; font-size: 9.8px; letter-spacing: .5px; color: var(--body-text); line-height: 13.4px; }
  .benefits li::before {
    content: ""; position: absolute; left: 0; top: 4px;
    border-left: 5px solid var(--body-text); border-top: 3px solid transparent; border-bottom: 3px solid transparent;
  }

  .stats { position: absolute; left: 339px; top: 257px; width: 255px; height: 34px; border-top: 1.5px solid var(--stat-rule); }
  .stat { position: absolute; top: 0; width: 50px; margin-left: -25px; text-align: center; color: var(--body-text); }
  .stat__value { display: block; font-family: "Ubuntu", sans-serif; font-weight: 700; font-size: 13px; line-height: 14px; margin-top: 4px; }
  .stat__value small { font-size: 7px; }
  .stat__label { display: block; font-family: "Montserrat", sans-serif; font-size: 7px; letter-spacing: .3px; margin-top: 4px; }
  .stat__rule { position: absolute; top: 0; width: 1.2px; height: 32px; background: var(--stat-rule); }
</style>
</head>
<body>
<div class="canvas">

  <!-- Violet edition -->
  <section class="label label--violet">
    <div class="label__backdrop" role="img" aria-label="Soft-focus photograph of glossy molecular spheres joined by thin links"></div>
    <div class="label__band label__band--top"></div>
    <div class="label__band label__band--bottom"></div>
    <div class="front-panel" role="img" aria-label="Close-up photograph of clear liquid bubbles"></div>
    <div class="tab tab--capacity"></div><div class="tab tab--age"></div>
    <div class="badge badge--capacity"><span class="badge__caption">CAPACITY</span><span class="badge__value">620g</span></div>
    <div class="badge badge--age"><span class="badge__caption">EVERYONE ABOVE</span><span class="badge__value">25+</span></div>
    <div class="brand"><span class="brand__name">Nuvella</span><span class="brand__tagline">Her Gün</span></div>
    <div class="product__kind">HDYROLYZED</div>
    <div class="product__name">COLLOGEN</div>
    <div class="product__sub">PEPTIDES</div>
    <div class="product__uses">HAIR&nbsp; I &nbsp;SKIN&nbsp; I &nbsp;NAILS&nbsp; I &nbsp;JOINTS*</div>
    <svg class="plate" viewBox="0 0 172 28" aria-hidden="true">
      <defs><linearGradient id="plateSilverA" x1="0" x2="1"><stop offset="0" stop-color="#9a9a9a"/><stop offset=".3" stop-color="#f4f4f4"/><stop offset=".7" stop-color="#ffffff"/><stop offset="1" stop-color="#bcbcbc"/></linearGradient></defs>
      <polygon points="0,0 172,0 154,28 0,28" fill="url(#plateSilverA)" stroke="#8a8a8a" stroke-width="1.2"/>
    </svg>
    <span class="plate__text">PLATINUM</span>
    <ul class="benefits"><li>HYDROLYZED COLLAGEN</li><li>HIGH ABSORPTION</li><li>HIGH-QUALITY MATERIAL</li></ul>
    <div class="stats">
      <div class="stat" style="left:12px"><span class="stat__value">0<small>G</small></span><span class="stat__label">SUGAR</span></div>
      <div class="stat__rule" style="left:37px"></div>
      <div class="stat" style="left:65px"><span class="stat__value">0<small>G</small></span><span class="stat__label">FAT</span></div>
      <div class="stat__rule" style="left:88px"></div>
      <div class="stat" style="left:117px"><span class="stat__value">0<small>G</small></span><span class="stat__label">CARISS</span></div>
      <div class="stat__rule" style="left:145px"></div>
      <div class="stat" style="left:177px"><span class="stat__value">11<small>G</small></span><span class="stat__label">PROTIN</span></div>
      <div class="stat__rule" style="left:202px"></div>
      <div class="stat" style="left:228px"><span class="stat__value">12<small>G</small></span><span class="stat__label">COLLEN</span></div>
    </div>
  </section>

  <!-- Silver edition -->
  <section class="label label--silver">
    <div class="label__backdrop" role="img" aria-label="Soft-focus grey photograph of glossy molecular spheres joined by thin links"></div>
    <div class="label__band label__band--top"></div>
    <div class="label__band label__band--bottom"></div>
    <div class="front-panel" role="img" aria-label="Close-up photograph of clear liquid bubbles"></div>
    <div class="tab tab--capacity"></div><div class="tab tab--age"></div>
    <div class="badge badge--capacity"><span class="badge__caption">CAPACITY</span><span class="badge__value">620g</span></div>
    <div class="badge badge--age"><span class="badge__caption">EVERYONE ABOVE</span><span class="badge__value">25+</span></div>
    <div class="brand"><span class="brand__name">Nuvella</span><span class="brand__tagline">Her Gün</span></div>
    <div class="product__kind">HDYROLYZED</div>
    <div class="product__name">COLLOGEN</div>
    <div class="product__sub">PEPTIDES</div>
    <div class="product__uses">HAIR&nbsp; I &nbsp;SKIN&nbsp; I &nbsp;NAILS&nbsp; I &nbsp;JOINTS*</div>
    <svg class="plate" viewBox="0 0 172 28" aria-hidden="true">
      <defs><linearGradient id="plateSilverB" x1="0" x2="1"><stop offset="0" stop-color="#9a9a9a"/><stop offset=".3" stop-color="#f4f4f4"/><stop offset=".7" stop-color="#ffffff"/><stop offset="1" stop-color="#bcbcbc"/></linearGradient></defs>
      <polygon points="0,0 172,0 154,28 0,28" fill="url(#plateSilverB)" stroke="#3a3a3a" stroke-width="1.6"/>
    </svg>
    <span class="plate__text">PLATINUM</span>
    <ul class="benefits"><li>HYDROLYZED COLLAGEN</li><li>HIGH ABSORPTION</li><li>HIGH-QUALITY MATERIAL</li></ul>
    <div class="stats">
      <div class="stat" style="left:12px"><span class="stat__value">0<small>G</small></span><span class="stat__label">SUGAR</span></div>
      <div class="stat__rule" style="left:37px"></div>
      <div class="stat" style="left:65px"><span class="stat__value">0<small>G</small></span><span class="stat__label">FAT</span></div>
      <div class="stat__rule" style="left:88px"></div>
      <div class="stat" style="left:117px"><span class="stat__value">0<small>G</small></span><span class="stat__label">CARISS</span></div>
      <div class="stat__rule" style="left:145px"></div>
      <div class="stat" style="left:177px"><span class="stat__value">11<small>G</small></span><span class="stat__label">PROTIN</span></div>
      <div class="stat__rule" style="left:202px"></div>
      <div class="stat" style="left:228px"><span class="stat__value">12<small>G</small></span><span class="stat__label">COLLEN</span></div>
    </div>
  </section>

</div>
</body>
</html>
```